Sleek and elegant promotional banner/sign for The Vellinor Law Firm

We need a design for promotional items like banners, signs, print ads, etc. that includes our firm name - "The Vellinor Law Firm" - and what we do. We advise businesses and individuals on legal matters; we represent individuals and businesses in litigation and transactions; we select and create business entities; we solve legal problems for individuals and businesses, etc. PLEASE DO NOT SIMPLY REPEAT THE PREVIOUS SENTENCE ON THE DESIGN. Please create a tag-line or brief description from ours. We need something that describes what we do in concise and creative manner while communicating trust and confidence. The banner must also include our basic contact information: 948.512-7740 (telephone) and vellinorlaw.com (website). You may use one or more of the attached images, but needn't use any with the right design. The design should be sleek and modern.

Target Market(s)

wealthy individuals and small business owners, entrepreneurs

Industry/Entity Type

Lawyer

Font styles to use
Sans Serif

Colors
33a6d7
0556a4
33b8a4

Requirements
Must have
• Firm name, contact information, BRIEF description of our services, sleek and elegant.
• Also, the design must be horizontal - not vertical.
Nice to have
• I'd like to use one of the images
Should not have
• Cliches

```html
<!DOCTYPE html>
<html lang="en">
<head>
<meta charset="utf-8">
<title>The Vellinor Law Firm — Banner</title>
<link rel="stylesheet" href="https://fonts.googleapis.com/css2?family=Jost:wght@300;400;500;600&display=swap">
<style>
  :root {
    --navy: #0a4f9e;
    --blue: #1479c6;
    --blue-light: #2a8fd4;
    --teal: #33b8a4;
    --silver: #c9cdd2;
    --white: #ffffff;
  }
  html, body {
    margin: 0;
    padding: 0;
    width: 1200px;
    height: 771px;
    overflow: hidden;
    background: var(--white);
  }
  .banner {
    position: relative;
    width: 1200px;
    height: 771px;
    overflow: hidden;
    font-family: "Jost", "Futura", sans-serif;
    color: var(--white);
  }
  .banner__bands {
    position: absolute;
    inset: 0;
    width: 1200px;
    height: 771px;
  }
  .firm-name {
    position: absolute;
    top: 74px;
    left: 0;
    width: 1200px;
    text-align: center;
    font-weight: 300;
    font-size: 88px;
    line-height: 1;
    letter-spacing: 0;
    margin: 0;
  }
  .tagline {
    position: absolute;
    top: 282px;
    left: 0;
    width: 1200px;
    text-align: center;
    margin: 0;
    line-height: 1;
  }
  .tagline__lead {
    display: block;
    font-weight: 300;
    font-size: 63px;
  }
  .tagline__main {
    display: block;
    margin-top: 18px;
    font-weight: 500;
    font-size: 64px;
  }
  .service {
    position: absolute;
    top: 478px;
    display: flex;
    align-items: center;
    height: 88px;
  }
  .service__icon {
    width: 74px;
    height: 74px;
    flex: none;
  }
  .service__divider {
    width: 2px;
    height: 78px;
    background: var(--white);
    margin: 0 20px 0 24px;
    flex: none;
  }
  .service__label {
    font-size: 40px;
    line-height: 42px;
    text-transform: uppercase;
    white-space: nowrap;
  }
  .service__label span { display: block; }
  .service__label .light { font-weight: 300; }
  .service__label .bold { font-weight: 600; }
  .service--business-law { left: 86px; }
  .service--litigation { left: 424px; }
  .service--estate { left: 792px; }
  .contact {
    position: absolute;
    top: 678px;
    left: 0;
    width: 1200px;
    display: flex;
    justify-content: center;
    align-items: center;
    gap: 34px;
    font-size: 54px;
    font-weight: 500;
    line-height: 1;
  }
  .contact__item {
    display: flex;
    align-items: center;
    gap: 16px;
  }
  .contact__icon {
    width: 46px;
    height: 46px;
    flex: none;
  }
</style>
</head>
<body>
<main class="banner">
  <svg class="banner__bands" viewBox="0 0 1200 771" preserveAspectRatio="none" aria-hidden="true">
    <defs>
      <linearGradient id="middleBand" x1="0" y1="0" x2="0" y2="1">
        <stop offset="0" stop-color="var(--blue-light)"/>
        <stop offset="1" stop-color="var(--blue)"/>
      </linearGradient>
    </defs>
    <rect x="0" y="0" width="1200" height="771" fill="var(--navy)"/>
    <path d="M0 246 Q600 180 1200 246 L1200 771 L0 771 Z" fill="var(--silver)"/>
    <path d="M0 262 Q600 196 1200 262 L1200 771 L0 771 Z" fill="url(#middleBand)"/>
    <path d="M0 636 Q600 568 1200 636 L1200 771 L0 771 Z" fill="var(--silver)"/>
    <path d="M0 652 Q600 584 1200 652 L1200 771 L0 771 Z" fill="var(--teal)"/>
  </svg>

  <h1 class="firm-name">THE VELLINOR LAW FIRM</h1>

  <p class="tagline">
    <span class="tagline__lead">WE SOLVE THE MOST</span>
    <span class="tagline__main">PUZZLING LEGAL PROBLEMS</span>
  </p>

  <div class="service service--business-law">
    <svg class="service__icon" viewBox="0 0 74 74" fill="none" stroke="#fff" stroke-width="3" stroke-linejoin="round" aria-hidden="true">
      <rect x="6" y="22" width="62" height="42" rx="4"/>
      <path d="M27 22 V14 H47 V22"/>
      <path d="M6 40 H68"/>
      <rect x="32" y="36" width="10" height="9"/>
    </svg>
    <div class="service__divider"></div>
    <div class="service__label"><span class="light">Business</span><span class="bold">Law</span></div>
  </div>

  <div class="service service--litigation">
    <svg class="service__icon" viewBox="0 0 74 74" fill="none" stroke="#fff" stroke-width="3" stroke-linejoin="round" aria-hidden="true">
      <path d="M6 24 L37 8 L68 24 Z"/>
      <path d="M14 30 V56"/>
      <path d="M29 30 V56"/>
      <path d="M45 30 V56"/>
      <path d="M60 30 V56"/>
      <path d="M8 58 H66"/>
      <path d="M4 66 H70"/>
    </svg>
    <div class="service__divider"></div>
    <div class="service__label"><span class="light">Business</span><span class="bold">Litigation</span></div>
  </div>

  <div class="service service--estate">
    <svg class="service__icon" viewBox="0 0 74 74" fill="none" stroke="#fff" stroke-width="3" stroke-linejoin="round" aria-hidden="true">
      <path d="M6 34 L37 8 L68 34"/>
      <path d="M14 28 V66 H60 V28"/>
      <path d="M30 66 V46 H44 V66"/>
    </svg>
    <div class="service__divider"></div>
    <div class="service__label"><span class="light">Estate</span><span class="bold">Planning</span></div>
  </div>

  <div class="contact">
    <div class="contact__item">
      <svg class="contact__icon" viewBox="0 0 46 46" fill="none" stroke="#fff" stroke-width="3" aria-hidden="true">
        <circle cx="23" cy="23" r="20"/>
        <path d="M15 13 L19 12 L22 18 L19 21 Q21 26 25 28 L28 25 L34 28 L33 32 Q29 35 24 32 Q15 27 13 18 Q13 15 15 13 Z" stroke-linejoin="round"/>
      </svg>
      <span class="contact__text">948.512-7740</span>
    </div>
    <div class="contact__item">
      <svg class="contact__icon" viewBox="0 0 46 46" fill="none" stroke="#fff" stroke-width="3" aria-hidden="true">
        <circle cx="23" cy="23" r="20"/>
        <ellipse cx="23" cy="23" rx="9" ry="20"/>
        <path d="M3 23 H43"/>
        <path d="M7 13 H39"/>
        <path d="M7 33 H39"/>
      </svg>
      <span class="contact__text">vellinorlaw.com</span>
    </div>
  </div>
</main>
</body>
</html>
```